New design for a physiotherapy clinic specializing in laser therapy

BrightPath Physiotherapy is a unique clinic specializing in laser therapy. The clinic is now 7 years old and has a well established reputation for patient care.

We are the largest laser physiotherapy clinic in Mississauga, ON, Canada. We use state of the art laser therapy equipment. Our knowledge base of how to use Low Level Laser Therapy in conjunction with traditional physiotherapy is what sets us apart. Nobody wants to live with pain and everyone wants to get better as quickly as possible. Our treatment methodology helps our patients return to normal lives quickly.

We want a website that communicates expertise, trust and shows that we care for our patients. We also want people to understand that the treatments are painless and speed up healing naturally.
Updates

Please include a location tab in your submission.  This page should have a map of our location and our phone number.

I do not want any white coat and stethoscope people. We do not see hospitalized patients. We use Vara-Kor NuvoTel laser web site www.nuvotelbeam.example please remove any images with other laser machines. I do not want "massage" therapy pictures as the main image. We treat post op total hip and knee replacements, rotator cuff injuries, osteoarthritic back pain patients, sprained ankles, degenerative disc disease problems as some of the more general injuries seen.

Industry/Entity Type

Clinic

Requirements
Must have
• We want to retain as much of the current content as possible. We will be looking at editing the content to make it shorter.

In addition to the current pages we want to add a blog page and link.

see our current site www.brightpathphysio.example
Nice to have
• Medical Images in the Whiplash and Auto Injuries should be re-drawn.

We want a clean, uncluttered look to the site.

Should not have
• Do not use illustrations of lasers shooting out or cutting. This is a "Cold" laser and does not cut. The laser procedure is gentle and soothing.

```html
<!DOCTYPE html>
<html lang="en">
<head>
<meta charset="utf-8">
<title>BrightPath Physiotherapy</title>
<link href="https://fonts.googleapis.com/css2?family=PT+Sans:ital,wght@0,400;0,700;1,400&display=swap" rel="stylesheet">
<style>
:root{
  --green:#5f9a16;
  --green-light:#8cc43a;
  --green-dark:#4d8a10;
  --orange:#ef7d12;
  --orange-light:#f9a53a;
  --ink:#3a3a3a;
  --text:#555;
  --muted:#888;
  --panel:#efefef;
  --footer:#6e6e6e;
  --footer-dark:#5b5b5b;
}
*{box-sizing:border-box;margin:0;padding:0}
html,body{width:957px;height:1200px;overflow:hidden;background:#fff}
body{font-family:"PT Sans",sans-serif;color:var(--text);position:relative;font-size:7px;line-height:1.75}
.abs{position:absolute}
h2{font-size:14px;color:var(--green);font-weight:700;text-transform:uppercase;letter-spacing:.1px}
.btn{position:absolute;display:flex;align-items:center;justify-content:center;width:116px;height:24px;border-radius:2px;background:linear-gradient(var(--green-light),var(--green));color:#fff;font-size:7.5px;box-shadow:0 1px 1px rgba(0,0,0,.25)}
/* header */
.logo{left:144px;top:24px;width:240px;height:60px}
.logo .mark{position:absolute;left:0;top:10px;width:14px;height:14px;border-radius:50%;background:var(--green-light)}
.logo .name{position:absolute;left:22px;top:2px;font-size:22px;letter-spacing:2.5px;color:var(--ink);font-weight:400;line-height:30px}
.logo .sub{position:absolute;left:115px;top:31px;font-size:10px;color:var(--muted);letter-spacing:.5px;line-height:12px}
.logo .tag{position:absolute;left:115px;top:45px;font-size:11px;color:var(--green);line-height:13px}
.contact{right:145px;top:20px;text-align:right;border-right:2px solid #ccc;padding-right:10px;width:240px}
.contact .feat{color:var(--green);font-weight:700;font-size:8px;line-height:14px}
.contact p{font-size:6.5px;color:#666;line-height:14px;white-space:nowrap}
.contact .tel{margin-top:4px;display:flex;justify-content:flex-end;gap:16px;font-size:6.5px;color:#666}
.contact .tel span{display:flex;align-items:center;gap:3px}
/* nav */
.nav{left:144px;top:96px;width:670px;height:29px;background:linear-gradient(#4a4a4a,#2e2e2e);display:flex;justify-content:space-around;align-items:center;border-radius:3px 3px 0 0}
.nav a{color:#fff;font-size:7.5px;text-decoration:none}
/* hero */
.hero{left:144px;top:125px;width:670px;height:249px;background:linear-gradient(90deg,#d7c9a8 0%,#e6e0c9 30%,#d8e4b4 55%,#b7d27a 85%,#9cc354 100%);overflow:hidden}
.hero .photo{position:absolute;left:0;top:0;width:300px;height:249px;background:radial-gradient(ellipse at 45% 45%,#ecd7c3 0%,#d4b899 40%,rgba(190,160,120,0) 75%)}
.hero .copy{position:absolute;left:350px;top:58px;width:300px}
.hero h1{font-size:30px;color:#3a3a3a;font-weight:700;line-height:36px}
.hero h3{font-size:16px;color:var(--green-dark);font-weight:700;line-height:24px}
.hero p{font-size:7.5px;color:#333;line-height:13px;margin-top:8px}
.dots{position:absolute;right:12px;bottom:11px;display:flex;gap:2px}
.dots i{width:5px;height:5px;background:#e8f0d4;display:block}
.dots i:first-child{background:var(--green)}
.services{left:144px;top:374px;width:670px;height:53px;background:linear-gradient(var(--green-light),var(--green));display:flex;border-radius:0 0 3px 3px}
.services div{flex:1;padding:12px 0 0 27px;border-right:1px solid rgba(255,255,255,.3);color:#fff;white-space:nowrap}
.services div:last-child{border:none;padding-left:20px}
.services b{display:block;font-size:8.5px;line-height:14px;font-weight:400}
.services i{font-size:8px}
/* content */
.img-block{position:absolute}
.who .img-block{left:144px;top:473px;width:217px;height:105px;background:linear-gradient(90deg,#d9d3cc,#eee6dd 45%,#e6c9a6 70%,#f3ead9)}
.who p{position:absolute;left:144px;top:589px;width:220px}
.news-item{position:absolute;left:386px;width:210px}
.news-item h4{font-size:7.5px;color:var(--ink);font-weight:700;line-height:12px;margin-bottom:3px}
.news-item em{color:var(--orange);font-size:7px}
.divider{position:absolute;left:386px;top:549px;width:210px;height:1px;background:#ddd}
.appt{left:618px;top:446px;width:196px;height:210px;background:var(--panel)}
.appt h2{position:absolute;left:27px;top:15px;font-size:13px}
.field{position:absolute;height:17px;background:#fff;border-radius:2px;font-size:5.5px;color:#999;padding:0 9px;display:flex;align-items:center;justify-content:space-between}
.cta{position:absolute;left:15px;top:162px;width:166px;height:32px;background:linear-gradient(var(--orange-light),var(--orange));color:#fff;font-size:10px;font-weight:700;display:flex;align-items:center;justify-content:center;border-radius:2px}
.arrows{display:flex;gap:6px;color:#aaa;font-size:13px}
.testi{left:144px;top:718px;width:670px;height:90px;background:linear-gradient(#f1f1f1,#fff)}
.testi .face{position:absolute;left:17px;top:14px;width:74px;height:64px;background:linear-gradient(135deg,#e9d3a8,#d9b48c 60%,#c99c74)}
.testi .q{position:absolute;font-size:32px;color:#ccc;line-height:1}
.testi h4{position:absolute;left:134px;top:17px;font-size:9px;color:var(--green)}
.testi p{position:absolute;left:134px;top:35px;width:520px;font-size:7px;line-height:12px}
.testi .by{position:absolute;left:135px;top:70px;color:var(--orange);font-style:italic;font-size:7px}
.about .img-block{left:144px;top:860px;width:136px;height:82px;background:radial-gradient(circle at 50% 70%,#e9a591 0%,#bcbcbc 35%,#7a7a7a 70%,#fff 100%)}
.about .p1{position:absolute;left:306px;top:856px;width:246px;line-height:12.3px}
.about .p2{position:absolute;left:144px;top:949px;width:410px;line-height:12.3px}
.spec h5{position:absolute;left:580px;top:860px;color:var(--orange);font-size:8.5px}
.spec .note{position:absolute;left:580px;top:876px;width:215px;font-size:6.5px;line-height:12px;text-transform:uppercase}
.spec .img-block{left:581px;top:908px;width:81px;height:68px;background:linear-gradient(135deg,#e8dcd0,#cdb59c 55%,#f0ece6)}
.spec p{position:absolute;left:677px;top:908px;width:137px;line-height:12.3px}
/* footer */
.footer{left:144px;top:1042px;width:670px;height:158px;background:var(--footer);color:#ddd}
.footer h3{position:absolute;font-size:10px;color:#fff;font-weight:700}
.footer ul{position:absolute;list-style:none;font-size:5.8px;line-height:13.6px;text-transform:uppercase}
.footer .bar{position:absolute;left:0;bottom:0;width:670px;height:28px;background:var(--footer-dark);font-size:5.8px;color:#ddd;display:flex;align-items:center;justify-content:center}
.social{position:absolute;left:539px;display:flex;align-items:center;gap:7px;font-size:6px}
.social i{display:block;width:20px;height:20px;border-radius:50%;background:#2c6aa5}
.email{position:absolute;left:383px;top:69px;width:130px;height:17px;background:#555;font-size:5.5px;color:#aaa;padding-left:10px;display:flex;align-items:center}
.sub-btn{position:absolute;left:384px;top:93px;width:70px;height:16px;background:linear-gradient(var(--green-light),var(--green));color:#fff;font-size:6px;font-weight:700;display:flex;align-items:center;justify-content:center;border:1px solid #aaa}
</style>
</head>
<body>

<header>
  <div class="abs logo">
    <span class="mark"></span>
    <span class="name">BRIGHTPATH</span>
    <span class="sub">Physiotherapy Inc.</span>
    <span class="tag">Treating You Better</span>
  </div>
  <div class="abs contact">
    <div class="feat">FEATURE OUR LOCATION</div>
    <p>Meadowvale Plaza, 4410 Glen Arbour Road, Mississauga,</p>
    <p>ON L5N 2R4 Two blocks south of Hwy 403 on Glen Arbour Rd</p>
    <div class="tel">
      <span><svg width="9" height="9" viewBox="0 0 10 10"><path d="M2 1l2 2-1 1.5c.7 1.3 1.6 2.2 2.9 2.9L7.4 6.4l2 2-1.4 1.4C4.5 9.5.5 5.5.6 2z" fill="#888"/></svg>Telephone : 905-555-0142</span>
      <span><svg width="9" height="9" viewBox="0 0 10 10"><rect x="2.5" y="1" width="5" height="3" fill="#888"/><rect x="1" y="4" width="8" height="4" fill="#888"/><rect x="2.5" y="7" width="5" height="2.5" fill="#bbb"/></svg>FAX : 905-555-0187</span>
    </div>
  </div>
</header>

<nav class="abs nav">
  <a>CLINIC HOURS</a><a>FAQ'S</a><a>LOCATION &amp; MAP</a><a>NEWS</a><a>PATIENT FORMS</a><a>EMPLOYMENT OPPORTUNITIES</a><a>TESTIMONIALS</a><a>BLOG</a>
</nav>

<section class="abs hero">
  <div class="photo" role="img" aria-label="Photo of a woman wearing a neck collar resting on a pillow"></div>
  <div class="copy">
    <h1>We are</h1>
    <h3>Mississauga's premier physiotherapy<br>and low intensity laser therapy specialists</h3>
    <p>We integrate physiotherapy with low intensity laser therapy (laser therapy, LILT or cold laser therapy) to safely and effectively treat a wide variety of musculoskeletal injuries and inflammatory conditions</p>
  </div>
  <div class="dots"><i></i><i></i><i></i><i></i><i></i></div>
</section>

<div class="abs services">
  <div><b>PHYSIOTHERAPY</b><i>Click here for More Info</i></div>
  <div><b>LASER THERAPY</b><i>Click here for More Info</i></div>
  <div><b>INSURANCE</b><i>Click here for More Info</i></div>
  <div><b>MASSAGE THERAPY</b><i>Click here for More Info</i></div>
  <div><b>WHIPLASH &amp; AUTO INJURIES</b><i>Click here for More Info</i></div>
</div>

<section class="who">
  <h2 class="abs" style="left:144px;top:444px">Who are we</h2>
  <div class="img-block" role="img" aria-label="Photo of a physiotherapist assessing a patient's neck"></div>
  <p>We are Mississauga's premier physiotherapy and low intensity laser therapy specialists. We integrate physiotherapy with low intensity laser therapy (laser therapy...</p>
  <a class="btn" style="left:144px;top:640px">Click here for More Info</a>
</section>

<section class="news">
  <h2 class="abs" style="left:384px;top:444px">Recent news</h2>
  <div class="news-item" style="top:471px">
    <h4>DRUG FREE PAIN RELIEF</h4>
    <p>Spring is here at last! After a long cold winter, we all want to get outside and enjoy the good weather. You look at your garden and grab a shovel. Or you dust off your golf clubs...</p>
    <em>Vital Years - May 2007</em>
  </div>
  <div class="divider"></div>
  <div class="news-item" style="top:559px">
    <h4>DRUG FREE PAIN RELIEF</h4>
    <p>Spring is here at last! After a long cold winter, we all want to get outside and enjoy the good weather. You look at your garden and grab a shovel. Or you dust off your golf clubs...</p>
    <em>Vital Years - May 2007</em>
  </div>
  <a class="btn" style="left:386px;top:640px">Click here for More News</a>
</section>

<aside class="abs appt">
  <h2>Make an appointment</h2>
  <div class="field" style="left:15px;top:45px;width:166px">NAME :</div>
  <div class="field" style="left:15px;top:72px;width:166px">EMAIL :</div>
  <div class="field" style="left:15px;top:99px;width:166px">PHONE :</div>
  <div class="field" style="left:15px;top:127px;width:79px">DATE :
    <svg width="9" height="10" viewBox="0 0 9 10"><rect x=".5" y="1" width="8" height="8.5" fill="#aaa"/><path d="M2 4h5M2 6h5M2 8h5" stroke="#fff" stroke-width=".8"/></svg></div>
  <div class="field" style="left:104px;top:127px;width:77px">TIME :
    <svg width="10" height="10" viewBox="0 0 10 10"><circle cx="5" cy="5" r="4" fill="none" stroke="#aaa" stroke-width="1.2"/><path d="M5 2.5V5h2" stroke="#aaa" fill="none"/></svg></div>
  <div class="cta">CONFORMED APPOINTMENT</div>
</aside>

<section>
  <h2 class="abs" style="left:144px;top:689px">Patient testimonials</h2>
  <div class="abs arrows" style="left:789px;top:692px"><span>&#8249;</span><span>&#8250;</span></div>
  <div class="abs testi">
    <div class="face" role="img" aria-label="Portrait photo of a smiling patient"></div>
    <span class="q" style="left:108px;top:12px">&ldquo;</span>
    <h4>LOW BACK PAIN, MUSCLE SPASM</h4>
    <p>I had pain in my lower back on the left side. The muscle spasms were so severe I could hardly walk. My wife, who had been a patient at BrightPath, told me to go see Marta and get laser therapy.</p>
    <div class="by">RTM &nbsp;&nbsp;|&nbsp;&nbsp; September 17, 2007</div>
    <span class="q" style="left:636px;top:58px">&rdquo;</span>
  </div>
</section>

<section class="about">
  <h2 class="abs" style="left:144px;top:831px">About BrightPath</h2>
  <div class="img-block" role="img" aria-label="Photo of a hand on a man's sore shoulder"></div>
  <p class="p1">When we combine laser therapy with traditional physiotherapy mobilization and strengthening, the results are remarkable. The treatment is pain free! And best of all you will heal faster, with superior tissue repair and range of motion.<br><br>Low Intensity Laser Therapy (LILT), also know as biophotostimulation, helps restore normal cellular function while enhancing the body's natural healing</p>
  <p class="p2">processes. The laser treatments are painless. Frequently, patients will experience a reduction in pain after their 1st treatment and sleep more soundly that evening.</p>
  <a class="btn" style="left:144px;top:986px">Click here for More Info</a>
</section>

<section class="spec">
  <h2 class="abs" style="left:579px;top:831px">Our specialist</h2>
  <div class="abs arrows" style="left:790px;top:827px"><span>&#8249;</span><span>&#8250;</span></div>
  <h5>DR. DANIEL WHITCOMBE'S</h5>
  <div class="note">This presentation may be slow to download but is worth the wait.</div>
  <div class="img-block" role="img" aria-label="Photo of the clinic specialist"></div>
  <p>When we combine laser therapy with traditional physiotherapy mobilization and strengthening, the results are remarkable. The treatment is pain free! And best of all you will heal faster...</p>
  <a class="btn" style="left:581px;top:992px">Click here for More Info</a>
</section>

<footer class="abs footer">
  <h3 style="left:20px;top:19px">QUICK LINKS</h3>
  <ul style="left:22px;top:40px"><li>Home</li><li>Contact Info</li><li>Clinic Hours</li><li>Visiting our Clinic - FAQ'S</li><li>Location &amp; Map</li></ul>
  <ul style="left:138px;top:40px"><li>Patient Forms</li><li>Employment Opportunities</li><li>BrightPath in the News</li><li>Testimonials</li><li>Blog</li></ul>
  <ul style="left:268px;top:40px"><li>Physiotherapy</li><li>Laser Therapy</li><li>Insurance</li><li>Massage Therapy</li><li>Whiplash &amp; Auto Injuries</li></ul>
  <h3 style="left:382px;top:19px">NEWSLETTER SIGNUP</h3>
  <div class="abs" style="left:383px;top:38px;font-size:5.8px;font-weight:700;color:#fff;line-height:12px">GET A RECENT UPDATE THROUGH<br>YOUR EMAIL</div>
  <div class="email">ENTER YOUR EMAIL ID</div>
  <div class="sub-btn">SUBSCRIBE</div>
  <h3 style="left:539px;top:19px">FOLLOW US</h3>
  <div class="social" style="top:42px"><i></i>FRIENDLINK</div>
  <div class="social" style="top:69px"><i style="background:#3a98c9"></i>CHIRPER</div>
  <div class="social" style="top:96px"><i style="background:#1f6e99"></i>PRONET</div>
  <div class="bar">COPYRIGHTS &copy; 2013. BRIGHTPATH. ALL RIGHTS RESERVED.</div>
</footer>

</body>
</html>
```